Brookvale Rendering Wordpress Design

I would like a design for my friends company. He has just had his logo designed and really likes the following website.

www.tlb-rendering.co.uk

Something similar to this design would be ideal but open to additional ideas. The website shown has all the relevant content.

We have 20 years of experience and can provide a number of photos for work we have done.

More photos will be provided upon request.

Target Market(s)

Homeowners

Industry/Entity Type

Trade

Font styles to use
Sans Serif

Colors
3176b5
85cae6
85abd2
eaf1f7

Requirements
Must have
• look at www.tlb-rendering.co.uk
Nice to have
Should not have
• N/A

```html
<!DOCTYPE html>
<html lang="en">
<head>
<meta charset="utf-8">
<title>Brookvale Rendering</title>
<link href="https://fonts.googleapis.com/css2?family=Raleway:wght@400;500;600;700&family=Open+Sans:ital,wght@0,400;0,600;0,700;1,400&display=swap" rel="stylesheet">
<style>
:root{
  --blue:#3176b5;
  --sky:#85cae6;
  --steel:#85abd2;
  --mist:#eaf1f7;
  --mist-dark:#dbe7f2;
  --deep:#2a68a3;
  --ink:#2b2b2b;
  --white:#fff;
}
*{box-sizing:border-box;margin:0;padding:0}
html,body{width:1200px;height:3232px;overflow:hidden}
body{position:relative;background:var(--white);font-family:"Open Sans",Arial,sans-serif;color:var(--ink)}
.abs{position:absolute}

/* top bar */
.topbar{top:0;left:0;width:1200px;height:47px;background:var(--white);border-bottom:1px solid #e6e6e6}
.social{display:flex;gap:9px}
.social span{width:17px;height:17px;background:var(--blue);border-radius:2px;display:block}
.contact-mini{top:13px;right:75px;display:flex;gap:26px;font-size:14px;color:var(--blue);align-items:center}
.contact-mini span{display:flex;align-items:center;gap:8px}

/* header */
.header{top:47px;left:0;width:1200px;height:93px;background:var(--white)}
.logo{left:75px;top:22px;display:flex;align-items:center;gap:10px;font-family:"Raleway",sans-serif;font-weight:700;font-size:24px;color:var(--blue);letter-spacing:.5px}
.logo i{width:14px;height:14px;background:var(--blue);display:block}
.nav{left:407px;top:39px;display:flex;align-items:center;font-size:15px;color:#333}
.nav a{color:#333;text-decoration:none;height:41px;line-height:41px;padding:0 22px;margin-right:24px}
.nav a.active{background:var(--blue);color:#fff;border-radius:2px;padding:0 25px}
.search{left:1084px;top:39px;width:41px;height:41px;background:#eee;display:flex;align-items:center;justify-content:center}

/* hero */
.hero{top:140px;left:0;width:1200px;height:489px;background:linear-gradient(120deg,#6e5f4f 0%,#b8aa96 35%,#d9d2c6 55%,#8d7d68 80%,#5b4c3d 100%)}
.hero-title{left:77px;top:330px;font-family:"Raleway",sans-serif;font-weight:600;font-size:42px;color:#fff;line-height:52px}
.hero-title span{display:inline-block;background:rgba(30,30,30,.55);padding:0 10px;margin-bottom:4px}
.dots{left:75px;top:566px;display:flex;gap:8px}
.dots i{width:11px;height:11px;border-radius:50%;background:#222;display:block}
.dots i.on{background:var(--sky)}
.quote-form{left:767px;top:220px;width:358px;height:330px;background:#fff;box-shadow:0 0 8px rgba(0,0,0,.25)}
.quote-form h3{background:var(--sky);color:#1d3f66;font-family:"Raleway",sans-serif;font-weight:600;font-size:24px;height:54px;line-height:54px;padding-left:18px}
.field{margin:14px 18px 0;height:40px;border:1px solid #ddd;font-size:13px;color:#888;line-height:38px;padding:0 14px;display:flex;justify-content:space-between}
.quote-form .submit{margin:18px 18px 0;height:44px;background:linear-gradient(#5d9bd6,var(--blue));color:#fff;font-weight:700;font-size:19px;text-align:center;line-height:44px;border-radius:2px}

/* plastered bands: flat soft fill standing in for the wall texture */
.band{left:0;width:1200px;background:linear-gradient(180deg,var(--mist) 0%,var(--mist-dark) 50%,var(--mist) 100%)}
.divider{left:502px;width:196px;height:3px;background:var(--blue)}
.sec-title{left:0;width:1200px;text-align:center;font-family:"Raleway",sans-serif;font-weight:500;font-size:28px;color:#222}
.center-text{text-align:center;font-size:14px;line-height:21px;color:#666}

/* welcome */
.welcome{top:629px;height:332px}
.learn{left:0;width:1200px;top:896px;text-align:center;font-family:"Raleway",sans-serif;font-weight:700;font-size:16px;color:var(--blue)}
.learn::after{content:"";display:block;width:40px;height:3px;background:var(--blue);margin:8px auto 0}

/* intro */
.video{left:75px;top:1006px;width:511px;height:313px;background:linear-gradient(135deg,#5d5f63 0%,#8a8f96 40%,#c8a24a 60%,#3f6aa8 85%,#2e3f5e 100%)}
.play{left:297px;top:1137px;width:66px;height:46px}
.intro h2{font-family:"Raleway",sans-serif;font-weight:500;font-size:28px;color:#222}
.intro h3{font-family:"Raleway",sans-serif;font-weight:700;font-size:22px;color:var(--blue);margin-top:6px}
.intro p{font-size:14px;line-height:24px;color:#666;margin-top:18px;width:510px}
.btn{background:var(--sky);color:#fff;font-size:15px;text-align:center;border-radius:2px}

/* services */
.services{top:1362px;height:573px}
.svc{width:310px;text-align:center}
.svc .icon{width:88px;height:88px;border-radius:50%;background:var(--blue);margin:0 auto;display:flex;align-items:center;justify-content:center}
.svc h4{font-family:"Raleway",sans-serif;font-weight:700;font-size:18px;color:var(--blue);margin-top:26px}
.svc p{font-size:14px;line-height:21px;color:#666;margin-top:10px}

/* works */
.work{top:2084px;height:230px}
.work-a{left:75px;width:341px;background:linear-gradient(160deg,#9fc0e6 0%,#b48a64 45%,#7a5a40 100%)}
.work-b{left:431px;width:341px;background:linear-gradient(160deg,#a9c6e4 0%,#8a8a86 50%,#5b5148 100%)}
.work-c{left:787px;width:340px;background:linear-gradient(160deg,#9a6b52 0%,#b79d84 45%,#cfc7bb 100%)}
.work-b::after{content:"";position:absolute;inset:0;background:rgba(133,171,210,.55)}

/* testimonials & partners */
.testimonial{top:2461px;left:0;width:601px;height:353px;background:var(--steel)}
.partners{top:2461px;left:601px;width:599px;height:353px;background:var(--sky)}
.panel-title{font-family:"Raleway",sans-serif;font-weight:500;font-size:26px;color:#fff}
.quote{left:136px;top:2551px;width:420px;font-style:italic;font-size:13.5px;line-height:24px;color:#fff}
.qmark{left:75px;top:2540px;font-family:Georgia,serif;font-size:60px;color:#fff;line-height:60px}
.avatar{left:75px;top:2692px;width:76px;height:76px;background:linear-gradient(135deg,#d9b79a,#8ea4bd)}
.person{left:168px;top:2718px;font-size:14px;line-height:22px}
.person b{font-weight:600;color:#2d3e55}
.person em{color:#2d3e55}
.arrows{display:flex;gap:10px}
.arrows i{width:17px;height:17px;border-radius:50%;background:#fff;display:flex;align-items:center;justify-content:center}
.badge{width:155px;height:73px;background:#fff}
.badge::after{content:"";position:absolute;left:35px;top:22px;width:85px;height:29px;background:#dfe9f2;border-radius:3px}

/* tweets */
.tweets-title{left:128px;top:2870px;font-family:"Raleway",sans-serif;font-weight:500;font-size:26px;color:#222}
.tweet{left:362px;top:2850px;width:720px;font-size:14px;line-height:26px;color:#666}
.tweet a{color:var(--blue);text-decoration:none}
.posted{left:362px;top:2910px;font-size:12px;font-style:italic;color:var(--blue)}

/* footer */
.footer{top:2948px;left:0;width:1200px;height:228px;background:var(--blue);color:#fff}
.fcol h5{font-family:"Raleway",sans-serif;font-weight:700;font-size:17px;margin-bottom:12px}
.fcol p,.fcol li{font-size:13.5px;line-height:21px;list-style:none;color:#e8f0f8}
.fcol li{line-height:26px}
.bottombar{top:3176px;left:0;width:1200px;height:56px;background:var(--deep);color:#fff;font-size:12px}
</style>
</head>
<body>

<div class="abs topbar">
  <div class="abs social" style="left:75px;top:14px"><span></span><span></span><span></span><span></span><span></span></div>
  <div class="abs contact-mini">
    <span><svg width="13" height="13" viewBox="0 0 24 24"><path fill="#3176b5" d="M6.6 10.8a15 15 0 0 0 6.6 6.6l2.2-2.2a1 1 0 0 1 1-.25 11.4 11.4 0 0 0 3.6.6 1 1 0 0 1 1 1V20a1 1 0 0 1-1 1A17 17 0 0 1 3 4a1 1 0 0 1 1-1h3.5a1 1 0 0 1 1 1c0 1.25.2 2.45.6 3.6a1 1 0 0 1-.25 1z"/></svg>1-800-555-0142</span>
    <span><svg width="14" height="11" viewBox="0 0 24 18"><rect width="24" height="18" rx="2" fill="#3176b5"/><path d="M1 2l11 8 11-8" stroke="#fff" stroke-width="2" fill="none"/></svg>info@brookvale-mail.co.uk</span>
  </div>
</div>

<header class="abs header">
  <div class="abs logo"><i></i>Brookvale Rendering</div>
  <nav class="abs nav">
    <a class="active">Home</a><a>About Us</a><a>Services</a><a>News &amp; Updates</a><a>Contact us</a>
  </nav>
  <div class="abs search"><svg width="16" height="16" viewBox="0 0 24 24"><circle cx="10" cy="10" r="7" stroke="#333" stroke-width="2.5" fill="none"/><path d="M15 15l6 6" stroke="#333" stroke-width="2.5"/></svg></div>
</header>

<section class="abs hero" role="img" aria-label="Interior room under renovation with freshly plastered walls, exposed beams and a wheelbarrow"></section>
<div class="abs hero-title"><span>Welcome to</span><br><span>Brookvale Rendering</span></div>
<div class="abs dots"><i class="on"></i><i></i><i></i><i></i></div>
<form class="abs quote-form">
  <h3>Request A Free Quotes</h3>
  <div class="field">Name</div>
  <div class="field">Phone No.</div>
  <div class="field">Subject<span>&#8693;</span></div>
  <div class="field">Email Address</div>
  <div class="submit">Submit &nbsp;Now</div>
</form>

<section class="abs band welcome" role="img" aria-label="Pale blue textured plaster wall background"></section>
<div class="abs divider" style="top:692px"></div>
<h2 class="abs sec-title" style="top:715px">Welcome to Our Website</h2>
<p class="abs center-text" style="left:95px;top:764px;width:1010px">Aliquam molestie, mi et imperdiet euismod, dui purus auctor tellus, et interdum lacus lectus et ante. Sed accumsan sollicitudin sapien, sit amet adipiscing turpis gravida ac. In congue, neque ac lobortis volutpat, libero mauris varius mi, vitae suscipit ipsum ligula vitae risus. Duis aliquam nibh a dui iaculis viverra id a velit. Vivamus egestas risus in magna varius commodo. Sed semper viverra egestas. Etiam pretium porttitor lectus, vel ornare neque porta volutpat.</p>
<div class="abs learn">Learn More</div>

<div class="abs video" role="img" aria-label="Plasterer in a hard hat smoothing a wall with a trowel, video thumbnail"></div>
<svg class="abs play" viewBox="0 0 66 46"><rect width="66" height="46" rx="8" fill="#fff"/><path d="M26 13l16 10-16 10z" fill="#333"/></svg>
<div class="abs intro" style="left:614px;top:996px">
  <h2>Are you looking for a Plasterer ?</h2>
  <h3>Brookvale Rendering Help You</h3>
  <p>Aliquam molestie, mi et imperdiet euismod, dui purus auctor tellus, et interdum lacus lectus et ante. Sed accumsan sollicitudin sapien, sit amet adipiscing turpis gravida ac. In congue, neque ac lobortis volutpat, libero mauris varius mi, vitae suscipit ipsum ligula vitae risus. Duis aliquam nibh a dui iaculis viverra id a velit.</p>
</div>
<div class="abs btn" style="left:614px;top:1237px;width:270px;height:47px;line-height:47px">Request Call For Free Quotes</div>

<section class="abs band services" role="img" aria-label="Pale blue textured plaster wall background"></section>
<div class="abs divider" style="top:1424px"></div>
<h2 class="abs sec-title" style="top:1450px">Our Services</h2>
<div class="abs svc" style="left:86px;top:1516px">
  <div class="icon"><svg width="40" height="40" viewBox="0 0 40 40"><path d="M4 20L20 6l16 14" stroke="#fff" stroke-width="3" fill="none"/><path d="M10 18v16h20V18" fill="#fff"/><rect x="17" y="24" width="6" height="10" fill="#3176b5"/></svg></div>
  <h4>Rendering</h4>
  <p>Sed accumsan sollicitudin sapien, sit amet adipiscing turpis gravida ac. In congue, neque ac lobortis volutpat, libero mauris varius mi, vitae suscipit ipsum ligula vitae risus.</p>
</div>
<div class="abs svc" style="left:446px;top:1516px">
  <div class="icon"><svg width="40" height="40" viewBox="0 0 40 40"><rect x="13" y="6" width="14" height="5" fill="#fff"/><rect x="15" y="11" width="10" height="16" fill="#fff"/><path d="M6 34l14-8 14 8z" fill="#fff"/></svg></div>
  <h4>Chimney Repairs</h4>
  <p>Sed accumsan sollicitudin sapien, sit amet adipiscing turpis gravida ac. In congue, neque ac lobortis volutpat, libero mauris varius mi, vitae suscipit ipsum ligula vitae risus.</p>
</div>
<div class="abs svc" style="left:806px;top:1516px">
  <div class="icon"><svg width="40" height="40" viewBox="0 0 40 40"><path d="M8 30l14-14 8 8-14 14z" fill="#fff"/><path d="M26 20l8-8" stroke="#fff" stroke-width="4" stroke-linecap="round"/></svg></div>
  <h4>Plasterboard / Dry Lining</h4>
  <p>Sed accumsan sollicitudin sapien, sit amet adipiscing turpis gravida ac. In congue, neque ac lobortis volutpat, libero mauris varius mi, vitae suscipit ipsum ligula vitae risus.</p>
</div>
<div class="abs btn" style="left:498px;top:1847px;width:207px;height:47px;line-height:47px">View All Services</div>

<div class="abs divider" style="top:1994px"></div>
<h2 class="abs sec-title" style="top:2016px">Recent Works</h2>
<div class="abs work work-a" role="img" aria-label="Stone house with a rounded tower after rendering work"></div>
<div class="abs work work-b" role="img" aria-label="Tudor-style house front with timber framing"></div>
<div class="abs work work-c" role="img" aria-label="Brick house wall base with fresh render finish"></div>
<svg class="abs" style="left:584px;top:2184px" width="34" height="34" viewBox="0 0 24 24"><circle cx="10" cy="10" r="7" stroke="#fff" stroke-width="2.5" fill="none"/><path d="M15 15l6 6" stroke="#fff" stroke-width="2.5"/></svg>
<div class="abs btn" style="left:498px;top:2368px;width:207px;height:46px;line-height:46px">View All Works</div>

<section class="abs testimonial"></section>
<h3 class="abs panel-title" style="left:75px;top:2496px">What Our Customers Says...</h3>
<div class="abs qmark">&#8220;</div>
<p class="abs quote">Aliquam molestie, mi et imperdiet euismod, dui purus auctor tellus, et interdum lacus lectus et ante. Sed accumsan sollicitudin sapien, sit amet adipiscing turpis gravida ac. In congue, neque ac lobortis volutpat, libero mauris varius mi, vitae suscipit ipsum ligula vitae risus..."</p>
<div class="abs avatar" role="img" aria-label="Customer portrait"></div>
<div class="abs person"><b>Tom Aldridge</b><br><em>Harlow Motor Works</em></div>
<div class="abs arrows" style="left:515px;top:2746px"><i><svg width="8" height="8" viewBox="0 0 8 8"><path d="M6 0L2 4l4 4" stroke="#3176b5" stroke-width="2" fill="none"/></svg></i><i><svg width="8" height="8" viewBox="0 0 8 8"><path d="M2 0l4 4-4 4" stroke="#3176b5" stroke-width="2" fill="none"/></svg></i></div>

<section class="abs partners"></section>
<h3 class="abs panel-title" style="left:642px;top:2496px">Proudly Working with Companies</h3>
<div class="abs badge" style="left:642px;top:2558px"></div>
<div class="abs badge" style="left:808px;top:2558px"></div>
<div class="abs badge" style="left:974px;top:2558px"></div>
<div class="abs badge" style="left:642px;top:2644px"></div>
<div class="abs badge" style="left:808px;top:2644px"></div>
<div class="abs badge" style="left:974px;top:2644px"></div>
<div class="abs arrows" style="left:1084px;top:2746px"><i><svg width="8" height="8" viewBox="0 0 8 8"><path d="M6 0L2 4l4 4" stroke="#3176b5" stroke-width="2" fill="none"/></svg></i><i><svg width="8" height="8" viewBox="0 0 8 8"><path d="M2 0l4 4-4 4" stroke="#3176b5" stroke-width="2" fill="none"/></svg></i></div>

<svg class="abs" style="left:128px;top:2848px" width="14" height="14" viewBox="0 0 14 14"><rect width="14" height="14" fill="#222"/></svg>
<h3 class="abs tweets-title">Recent Tweets</h3>
<p class="abs tweet">Aliquam molestie, mi et imperdiet euismod, dui purus auctor tellus, et interdum lacus lectus et ante. Sed accumsan <a>http://brkvl.link/a7d</a> sollicitudin sapien, sit amet adipiscing turpis gravida ac.</p>
<div class="abs posted">Posted on 3 hrs ago</div>

<footer class="abs footer">
  <div class="abs fcol" style="left:84px;top:36px;width:240px">
    <h5>About Brookvale</h5>
    <p>Lorem ipsum dolor sit amet, consect- etuer adipiscing elit, sed diam nonummy nibh euismod tincidunt ut laoreet dolore magna aliquam erat volutpat</p>
  </div>
  <div class="abs fcol" style="left:394px;top:36px">
    <h5>Company</h5>
    <ul><li>Home</li><li>About Us</li><li>Services</li><li>News &amp; Updates</li><li>Contact us</li></ul>
  </div>
  <div class="abs fcol" style="left:629px;top:36px">
    <h5>Services</h5>
    <ul><li>Duis aliquam</li><li>Nibh a dui iaculis</li><li>Vivamus egestas</li><li>Commodo</li><li>Sed semper</li></ul>
  </div>
  <div class="abs fcol" style="left:853px;top:36px;width:220px">
    <h5>Contact Us</h5>
    <p>42 Elmfield Road,<br>Leeds, LS2 7QT</p>
    <p style="margin-top:10px">&#9742;&nbsp; 1-800-555-0142</p>
    <p>&#9993;&nbsp; info@brookvale-mail.co.uk</p>
  </div>
</footer>
<div class="abs bottombar">
  <div class="abs" style="left:82px;top:20px">Copyright © 2016. Brookvale Rendering All Right Reserved</div>
  <div class="abs social" style="left:970px;top:18px;gap:13px"><span style="background:#9cc2e6"></span><span style="background:#9cc2e6"></span><span style="background:#9cc2e6"></span><span style="background:#9cc2e6"></span><span style="background:#9cc2e6"></span></div>
</div>

</body>
</html>
```